Painting Company Business Card

Brightwell Painting needs a new business card. See attachments for our logo and current card as an example.
We want to utilize the same colors in the logo, and keep all the information that is currently on it. Just need an updated and modern design.
We are open to loosing the Association Logos if it means a better design.
We are also entertaining a spot for a picture of a headshot of the person listed on the card. Head shot can be finished later.

```html
<!DOCTYPE html>
<html lang="en">
<head>
<meta charset="utf-8">
<title>Brightwell Painting – Business Card Concepts</title>
<link href="https://fonts.googleapis.com/css2?family=Source+Sans+3:ital,wght@0,400;0,600;0,700;1,700&display=swap" rel="stylesheet">
<style>
  :root {
    --stage: #2f2f30;
    --paper: #ffffff;
    --forest: #3d4a35;
    --leaf: #2f5a2c;
    --brick: #6b3c38;
    --slate: #8a8789;
    --signal: #c6323c;
    --badge: #9fb3c8;
    --badge-alt: #c9a4a4;
    --text-font: "Source Sans 3", "Myriad Pro", sans-serif;
  }
  * { box-sizing: border-box; margin: 0; padding: 0; }
  html, body { width: 1200px; height: 805px; overflow: hidden; }
  body { background: var(--stage); font-family: var(--text-font); position: relative; }

  .card {
    position: absolute; width: 523px; height: 314px;
    background: var(--paper); overflow: hidden;
  }
  .card--split-front { left: 55px; top: 27px; }
  .card--split-back  { left: 624px; top: 27px; }
  .card--swoosh-front { left: 55px; top: 438px; }
  .card--swoosh-back  { left: 642px; top: 443px; }

  .card svg.shape { position: absolute; inset: 0; width: 100%; height: 100%; }

  /* wordmark */
  .wordmark { position: absolute; color: var(--forest); font-weight: 700; line-height: 0.95; }
  .wordmark__line1 { display: block; font-size: 44px; letter-spacing: -1px; }
  .wordmark__line2 { display: block; font-size: 36px; letter-spacing: 1px; text-transform: uppercase; }

  /* name block */
  .person { position: absolute; text-align: center; }
  .person__name { font-size: 21px; font-weight: 700; color: var(--forest); }
  .person__role { font-size: 21px; font-weight: 400; color: var(--brick); }

  /* contact */
  .contact { position: absolute; list-style: none; color: var(--brick); }
  .contact li { display: flex; align-items: center; white-space: nowrap; }
  .contact__icon { flex: none; }

  /* services */
  .services {
    position: absolute; list-style: none; color: var(--paper);
    font-weight: 700; font-style: italic; text-align: center;
    font-size: 26px; line-height: 35px;
  }
  .website { position: absolute; color: var(--paper); font-size: 16px; }

  /* partner badges */
  .badges { position: absolute; }
  .badge { position: absolute; background: var(--badge); border-radius: 3px; }
  .badge--alt { background: var(--badge-alt); }

  /* card 1 */
  .card--split-front .wordmark { left: 14px; top: 108px; }
  .card--split-front .person { left: 320px; top: 18px; width: 200px; }
  .card--split-front .contact { left: 286px; top: 122px; font-size: 15px; }
  .card--split-front .contact li { margin-bottom: 16px; }
  .card--split-front .contact__icon { margin-right: 12px; }

  /* card 2 */
  .card--split-back .wordmark { left: 22px; top: 110px; }
  .card--split-back .services { left: 290px; top: 90px; width: 230px; }
  .card--split-back .website { left: 290px; top: 275px; width: 230px; text-align: center; }

  /* card 3 */
  .card--swoosh-front .wordmark { left: 290px; top: 30px; }
  .card--swoosh-front .person { left: 350px; top: 182px; width: 170px; }
  .card--swoosh-front .contact { left: 22px; top: 172px; color: var(--paper); font-size: 16px; }
  .card--swoosh-front .contact li { margin-bottom: 9px; }
  .card--swoosh-front .contact__icon { margin-right: 6px; }

  /* card 4 */
  .card--swoosh-back .wordmark { left: 24px; top: 200px; }
  .card--swoosh-back .services { left: 290px; top: 50px; width: 230px; }
  .card--swoosh-back .website {
    left: 505px; top: 290px; transform-origin: 0 0; transform: rotate(-90deg);
    font-style: italic; font-size: 15px;
  }
</style>
</head>
<body>

<!-- Concept A · front -->
<section class="card card--split-front">
  <svg class="shape" viewBox="0 0 523 314" aria-hidden="true">
    <path d="M275 0 H302 V72 A13.5 13.5 0 0 1 275 72 Z" fill="var(--forest)"/>
    <path d="M275 245 A13.5 13.5 0 0 1 302 245 V314 H275 Z" fill="var(--forest)"/>
  </svg>
  <div class="wordmark"><span class="wordmark__line1">Brightwell</span><span class="wordmark__line2">Painting</span></div>
  <div class="person">
    <p class="person__name">Daniel Hart</p>
    <p class="person__role">Quality Manager</p>
  </div>
  <ul class="contact">
    <li>
      <svg class="contact__icon" width="32" height="32" viewBox="0 0 32 32" aria-hidden="true">
        <circle cx="16" cy="16" r="14.5" fill="none" stroke="var(--forest)" stroke-width="1.6"/>
        <rect x="11.5" y="8" width="9" height="16" rx="1.5" fill="none" stroke="var(--brick)" stroke-width="1.6"/>
        <circle cx="16" cy="21" r="0.9" fill="var(--brick)"/>
      </svg>
      <span>262-555-0147</span>
    </li>
    <li>
      <svg class="contact__icon" width="32" height="32" viewBox="0 0 32 32" aria-hidden="true">
        <circle cx="16" cy="16" r="14.5" fill="none" stroke="var(--forest)" stroke-width="1.6"/>
        <rect x="7" y="14" width="10" height="6" rx="3" transform="rotate(-35 12 17)" fill="none" stroke="var(--forest)" stroke-width="1.6"/>
        <rect x="15" y="11" width="10" height="6" rx="3" transform="rotate(-35 20 14)" fill="none" stroke="var(--forest)" stroke-width="1.6"/>
      </svg>
      <span>Dan.Hart@mailbox.com<br>BrightwellPainting.com</span>
    </li>
  </ul>
</section>

<!-- Concept A · back -->
<section class="card card--split-back">
  <svg class="shape" viewBox="0 0 523 314" aria-hidden="true">
    <path d="M235 0 L252 6 L258 18 L250 30 L262 44 L256 60 L270 78 L262 96 L276 118 L268 140 L282 160 L274 182 L288 204 L280 228 L292 250 L284 272 L296 292 L290 314 H523 V0 Z" fill="var(--brick)"/>
  </svg>
  <div class="wordmark"><span class="wordmark__line1">Brightwell</span><span class="wordmark__line2">Painting</span></div>
  <div class="badges" aria-label="Partner associations">
    <span class="badge" style="left:50px;top:255px;width:26px;height:44px"></span>
    <span class="badge" style="left:84px;top:254px;width:50px;height:20px"></span>
    <span class="badge" style="left:146px;top:240px;width:40px;height:30px"></span>
    <span class="badge" style="left:194px;top:240px;width:24px;height:34px"></span>
    <span class="badge badge--alt" style="left:94px;top:282px;width:36px;height:20px"></span>
    <span class="badge badge--alt" style="left:142px;top:284px;width:44px;height:18px"></span>
  </div>
  <ul class="services">
    <li>Exterior Painting</li>
    <li>Interior Painting</li>
    <li>Carpentry</li>
    <li>Drywall</li>
  </ul>
  <p class="website">BrightwellPainting.com</p>
</section>

<!-- Concept B · front -->
<section class="card card--swoosh-front">
  <svg class="shape" viewBox="0 0 523 314" aria-hidden="true">
    <path d="M0 0 H45 C120 85 230 190 300 314 H0 Z" fill="var(--leaf)"/>
    <path d="M60 0 H100 C150 55 195 88 240 95 C285 102 310 150 345 220 C367 262 392 296 414 314 H335 C305 262 280 215 258 182 C215 130 140 80 60 0 Z" fill="var(--brick)"/>
    <path d="M180 0 H198 C210 40 222 70 240 95 C220 80 196 45 180 0 Z" fill="var(--slate)"/>
    <path d="M100 0 H130 C170 50 200 80 240 95 C190 88 150 55 100 0 Z" fill="var(--leaf)"/>
  </svg>
  <div class="wordmark"><span class="wordmark__line1">Brightwell</span><span class="wordmark__line2">Painting</span></div>
  <div class="person">
    <p class="person__name">Daniel Hart</p>
    <p class="person__role">Quality Manager</p>
  </div>
  <ul class="contact">
    <li>
      <svg class="contact__icon" width="34" height="34" viewBox="0 0 34 34" aria-hidden="true">
        <circle cx="17" cy="17" r="16" fill="var(--signal)" stroke="var(--paper)" stroke-width="2"/>
        <rect x="9" y="11" width="16" height="12" rx="1" fill="none" stroke="var(--paper)" stroke-width="1.6"/>
        <path d="M9 11 L17 18 L25 11" fill="none" stroke="var(--paper)" stroke-width="1.6"/>
      </svg>
      <span>262-555-0147</span>
    </li>
    <li>
      <svg class="contact__icon" width="34" height="34" viewBox="0 0 34 34" aria-hidden="true">
        <circle cx="17" cy="17" r="16" fill="var(--signal)" stroke="var(--paper)" stroke-width="2"/>
        <rect x="12" y="8" width="10" height="18" rx="1.5" fill="none" stroke="var(--paper)" stroke-width="1.6"/>
        <circle cx="17" cy="23" r="1" fill="var(--paper)"/>
      </svg>
      <span>Dan.Hart@mailbox.com</span>
    </li>
    <li>
      <svg class="contact__icon" width="34" height="34" viewBox="0 0 34 34" aria-hidden="true">
        <circle cx="17" cy="17" r="16" fill="var(--signal)" stroke="var(--paper)" stroke-width="2"/>
        <circle cx="17" cy="17" r="8" fill="none" stroke="var(--paper)" stroke-width="1.6"/>
        <ellipse cx="17" cy="17" rx="3.5" ry="8" fill="none" stroke="var(--paper)" stroke-width="1.3"/>
        <path d="M9 17 H25" stroke="var(--paper)" stroke-width="1.3"/>
      </svg>
      <span>BrightwellPainting.com</span>
    </li>
  </ul>
</section>

<!-- Concept B · back -->
<section class="card card--swoosh-back">
  <svg class="shape" viewBox="0 0 523 314" aria-hidden="true">
    <path d="M60 0 H523 V314 H420 C380 230 330 180 280 150 C200 100 120 60 60 0 Z" fill="var(--brick)"/>
    <path d="M170 0 H190 C230 70 285 110 330 150 C370 200 400 260 425 314 H392 C362 250 300 190 250 140 C205 98 182 50 170 0 Z" fill="var(--leaf)"/>
    <path d="M392 314 C372 270 350 240 325 210 C355 235 380 270 400 314 Z" fill="var(--slate)"/>
    <path d="M425 314 C405 270 390 240 370 215 C400 240 425 275 445 314 Z" fill="var(--leaf)"/>
  </svg>
  <div class="badges" aria-label="Partner associations">
    <span class="badge" style="left:32px;top:132px;width:22px;height:36px"></span>
    <span class="badge" style="left:60px;top:132px;width:40px;height:16px"></span>
    <span class="badge" style="left:104px;top:122px;width:30px;height:24px"></span>
    <span class="badge" style="left:140px;top:124px;width:20px;height:26px"></span>
    <span class="badge badge--alt" style="left:68px;top:154px;width:28px;height:16px"></span>
    <span class="badge badge--alt" style="left:104px;top:156px;width:30px;height:14px"></span>
  </div>
  <div class="wordmark"><span class="wordmark__line1">Brightwell</span><span class="wordmark__line2">Painting</span></div>
  <ul class="services">
    <li>Exterior Painting</li>
    <li>Interior Painting</li>
    <li>Carpentry</li>
    <li>Drywall</li>
  </ul>
  <p class="website">BrightwellPainting.com</p>
</section>

</body>
</html>
```